Two sided business card template for:

Nook 4 Keeps Storage
1873 Brindle Avenue,
Saskatoon, SK
S4R 2M6
306-517-3482
www.nook4keeps.ca

Front side should be standard business card information. Sample should be for Darren Kowalchuk, Operations Manager, darren@nook4keeps.ca

Back side should be an advertisement for the storage facility. Some points about our facility are below you may use some or all of these features in the ad.

-Online payments and bookings
-Seasonal bicycle, tire, and motorcycle storage
-24hr self storage access
-Safe, and secure, with digital video surveillance
-Airport location

Card could have, but doesn't need a clever tag line containing the company name

Finished design must be in Microsoft word, or publisher format, and text must be editable.

```html
<!DOCTYPE html>
<html lang="en">
<head>
<meta charset="utf-8">
<title>Nook 4 Keeps Storage – Business Card</title>
<link href="https://fonts.googleapis.com/css2?family=Caladea:wght@400;700&display=swap" rel="stylesheet">
<style>
  :root {
    --stage: #ecebe8;
    --paper: #ffffff;
    --ink: #1c1c1c;
    --brand-red: #d81f1f;
    --tint: #fbe9e2;
    --band-text: #ffffff;
  }
  * { box-sizing: border-box; margin: 0; padding: 0; }
  html, body {
    width: 1200px; height: 960px; overflow: hidden;
    background: var(--stage);
    font-family: "Caladea", Cambria, Georgia, serif;
    color: var(--ink);
  }
  .sheet {
    width: 1200px; height: 960px;
    display: flex; justify-content: center; align-items: center; gap: 90px;
  }
  .card {
    position: relative;
    width: 380px; height: 664px;
    background: var(--paper);
    box-shadow: 0 2px 3px rgba(0,0,0,.12), 0 12px 28px rgba(0,0,0,.12);
    overflow: hidden;
  }

  /* brand lockup */
  .brand {
    display: flex; align-items: center; gap: 12px;
    justify-content: center;
  }
  .brand-square {
    width: 34px; height: 34px; flex: none;
    background: var(--brand-red);
  }
  .brand-name {
    font-size: 28px; font-weight: 700; line-height: 1.05;
    color: var(--ink);
  }

  /* back side */
  .card-back .features {
    list-style: none;
    position: absolute; top: 62px; left: 44px; right: 30px;
    font-size: 15.5px; line-height: 1.38;
  }
  .card-back .brand {
    position: absolute; left: 0; right: 0; bottom: 110px;
  }

  /* front side */
  .card-front .tint-panel {
    position: absolute; left: 40px; right: 40px; top: 90px; bottom: 84px;
    background: var(--tint);
  }
  .card-front .brand {
    position: absolute; left: 0; right: 0; top: 44px;
  }
  .card-front .identity {
    position: absolute; left: 0; right: 0; top: 186px;
    text-align: center;
  }
  .person-name { font-size: 25px; font-weight: 700; letter-spacing: .3px; }
  .person-title { font-size: 15px; color: var(--brand-red); margin-top: 2px; }
  .contact {
    position: absolute; left: 0; right: 0; top: 300px;
    text-align: center;
    font-size: 18px; font-weight: 700; line-height: 1.45;
  }
  .address-band {
    position: absolute; left: 0; right: 0; bottom: 0; height: 84px;
    background: var(--brand-red);
    display: flex; align-items: center; justify-content: center;
    color: var(--band-text); font-size: 16px;
  }
</style>
</head>
<body>
<main class="sheet">
  <section class="card card-back" aria-label="Card back">
    <ul class="features">
      <li>-Online payments and bookings</li>
      <li>-Seasonal bicycle, tire, and motorcycle storage</li>
      <li>-24hr self storage access</li>
      <li>-Safe, and secure, with digital video surveillance</li>
      <li>-Airport location</li>
    </ul>
    <div class="brand">
      <span class="brand-square" aria-hidden="true"></span>
      <span class="brand-name">Nook 4 Keeps<br>Storage</span>
    </div>
  </section>

  <section class="card card-front" aria-label="Card front">
    <div class="tint-panel" aria-hidden="true"></div>
    <div class="brand">
      <span class="brand-square" aria-hidden="true"></span>
      <span class="brand-name">Nook 4 Keeps<br>Storage</span>
    </div>
    <div class="identity">
      <p class="person-name">Darren Kowalchuk</p>
      <p class="person-title">Operations Manager</p>
    </div>
    <div class="contact">
      <p>306-517-3482</p>
      <p>www.nook4keeps.ca</p>
      <p>darren@nook4keeps.ca</p>
    </div>
    <div class="address-band">1873 Brindle Avenue, Saskatoon, SK S4R 2M6</div>
  </section>
</main>
</body>
</html>
```